Financial Advisor Resource Firm needs business card design

Need business card design for company in Omaha NE called Tallowbrook Partners. We provide resources to financial advisors....workshop programs, retirement analysis, and insurance planning. I would like to see designs that use grays, greens, black, and white colors. The final design should communicate 'collaboration' and be simple yet attractive to financial planning clients. I will attached our logo and another picture of a puzzle piece coming together. I would like the incorporate the puzzle picture somehow, maybe on the back somehow, with color or just the gray scale....OR, the picture be the front of the card with 'Tallowbrook' definition on it (see upload) and then company logo, employee name, title, address on the back (see ppt uploaded). The following disclosure needs to be included somewhere- Advisory services offered through Marlowe Ridge Advisors, LLC.
Updates

I uploaded a svg and ai file of the logo

Target Market(s)

Financial planning clients and financial advisors....so pretty diverse age range of about 40-70.

Industry/Entity Type

Financial Planning

Contact Information for Business Card

Dennis K. Holloway, MBA
Founder/President
5727 E. Larkspur Avenue
Suite 418
Omaha, NE 68297
Phone- (402) 555-0147
Cell- (402) 555-0183
Fax- (402) 555-0129
email- dennis@tallowbrookgroup.example
web address- www.tallowbrookgroup.example

Colors
1b1b1b
474747
d3d3d3
ffffff
9bcb3c
abd036

Requirements
Must have
• Must include logo provided, must be 2 sided, and must have disclosure...all of these items listed in project description

```html
<!DOCTYPE html>
<html lang="en">
<head>
<meta charset="utf-8">
<title>Tallowbrook Partners – Business Card</title>
<link href="https://fonts.googleapis.com/css2?family=Lato:wght@400;700&display=swap" rel="stylesheet">
<style>
  :root {
    --ink: #1b1b1b;
    --charcoal: #474747;
    --mist: #d3d3d3;
    --paper: #ececec;
    --white: #ffffff;
    --leaf: #86c43a;
    --leaf-bright: #9bcb3c;
    --backdrop: #8c8c8c;
  }
  * { box-sizing: border-box; margin: 0; padding: 0; }
  html, body { width: 1200px; height: 1200px; overflow: hidden; }
  body {
    background: var(--backdrop);
    font-family: "Lato", Arial, sans-serif;
    position: relative;
  }
  .card {
    position: absolute;
    top: 310px;
    width: 366px;
    height: 594px;
    box-shadow: 0 3px 6px rgba(0,0,0,0.35);
    overflow: hidden;
  }
  .card--front { left: 233px; background: var(--paper); color: var(--ink); text-align: center; }
  .card--back { left: 628px; background: var(--leaf); }

  .brand {
    position: absolute;
    left: 0; right: 0;
    display: flex; align-items: center; justify-content: center; gap: 10px;
    white-space: nowrap;
  }
  .brand__mark { flex: 0 0 auto; width: 16px; height: 16px; border-radius: 50%; background: var(--leaf); }
  .brand__name { font-weight: 700; letter-spacing: 0.5px; color: var(--ink); line-height: 1; }

  .front__brand { top: 140px; }
  .front__brand .brand__name { font-size: 22px; }

  .person { position: absolute; top: 263px; left: 0; right: 0; }
  .person__name { color: var(--leaf); font-size: 19px; font-weight: 700; line-height: 24px; }
  .person__name small { font-size: 17px; font-weight: 400; }
  .person__title { font-size: 16px; line-height: 20px; }

  .divider {
    position: absolute; left: 0; right: 0;
    display: flex; align-items: center; justify-content: center; gap: 6px;
  }
  .divider::before, .divider::after {
    content: ""; width: 56px; height: 1px; background: var(--ink);
  }
  .divider svg { width: 24px; height: 24px; }

  .info { position: absolute; left: 0; right: 0; font-size: 16px; line-height: 20px; }

  .back__dark { position: absolute; inset: 0; }
  .back__brand { top: 268px; }
  .back__brand .brand__name { color: var(--white); font-size: 24px; }
  .back__brand .brand__mark { background: var(--white); }
  .disclosure {
    position: absolute; top: 511px; left: 0; right: 0;
    text-align: center; color: var(--white); font-size: 16px; line-height: 21px;
  }
</style>
</head>
<body>

<section class="card card--front">
  <div class="brand front__brand">
    <span class="brand__mark"></span>
    <span class="brand__name">TALLOWBROOK PARTNERS</span>
  </div>

  <div class="person">
    <p class="person__name">DENNIS K. HOLLOWAY, <small>MBA</small></p>
    <p class="person__title">Founder/President</p>
  </div>

  <div class="divider" style="top:316px">
    <svg viewBox="0 0 24 24" aria-label="Phone">
      <circle cx="12" cy="12" r="10.5" fill="none" stroke="var(--leaf)" stroke-width="1.6"/>
      <path d="M8.6 7.2l1.6-.4 1 2.4-1 .8c.5 1.2 1.4 2.1 2.6 2.6l.8-1 2.4 1-.4 1.6c-3.6.2-7.2-3.4-7-7z" fill="var(--leaf)"/>
    </svg>
  </div>
  <div class="info" style="top:343px">
    <p>(402) 555-0147</p>
    <p>(402) 555-0183</p>
    <p>(402) 555-0129</p>
  </div>

  <div class="divider" style="top:409px">
    <svg viewBox="0 0 24 24" aria-label="Web">
      <circle cx="12" cy="12" r="10.5" fill="none" stroke="var(--leaf)" stroke-width="1.6"/>
      <circle cx="12" cy="12" r="6" fill="var(--leaf)"/>
      <path d="M6 12h12M12 6c-2.5 3-2.5 9 0 12M12 6c2.5 3 2.5 9 0 12" stroke="var(--paper)" stroke-width="1" fill="none"/>
    </svg>
  </div>
  <div class="info" style="top:435px">
    <p>dennis@tallowbrookgroup.example</p>
    <p>www.tallowbrookgroup.example</p>
  </div>

  <div class="divider" style="top:482px">
    <svg viewBox="0 0 24 24" aria-label="Location">
      <circle cx="12" cy="12" r="10.5" fill="none" stroke="var(--leaf)" stroke-width="1.6"/>
      <path d="M12 18s-4.5-4.6-4.5-7.5a4.5 4.5 0 019 0C16.5 13.4 12 18 12 18z" fill="var(--leaf)"/>
      <circle cx="12" cy="10.5" r="1.7" fill="var(--paper)"/>
    </svg>
  </div>
  <div class="info" style="top:512px">
    <p>5727 E. Larkspur Avenue</p>
    <p>Suite 418 Omaha, NE 68297</p>
  </div>
</section>

<section class="card card--back">
  <svg class="back__dark" viewBox="0 0 366 594" preserveAspectRatio="none" aria-hidden="true">
    <path d="M0 0H366V270C320 360 240 430 150 425C80 420 30 380 0 340Z" fill="var(--ink)"/>
  </svg>
  <div class="brand back__brand">
    <span class="brand__mark"></span>
    <span class="brand__name">TALLOWBROOK</span>
  </div>
  <p class="disclosure">ADVISORY SERVICES OFFERED<br>THROUGH MARLOWE RIDGE ADVISORS, LLC.</p>
</section>

</body>
</html>
```